Need Powerpoint masters for my consulting company in privacy (RGPD) and IT

For my newly created consulting company I need powerpoint slides masters.
The company is specialzed in privacy (RGPD) and IT.
The company already has a logo (obtained via Pixelhive).
These master slides will be mainly used when presenting reports/analysis to clients.
I'll attach a PNG files of the logo.

```html
<!DOCTYPE html>
<html lang="en">
<head>
<meta charset="utf-8">
<title>Maren Aubel Conseil – Slide Masters</title>
<link href="https://fonts.googleapis.com/css2?family=Lato:wght@300;400;700&display=swap" rel="stylesheet">
<style>
:root{
  --navy:#0a3150;
  --navy-deep:#06243c;
  --teal:#0f8c9d;
  --teal-light:#a9dbe2;
  --teal-bright:#25a9b9;
  --grey:#a7a7a7;
  --grey-light:#e2e2e2;
  --grid:#eeeeee;
  --ink:#1f2b36;
  --body:#9aa3ab;
  --white:#ffffff;
}
*{box-sizing:border-box;margin:0;padding:0}
html,body{width:1200px;height:2400px;overflow:hidden;background:#f1f3f5}
body{position:relative;font-family:'Lato',sans-serif;color:var(--ink)}
.slide{position:absolute;width:588px;height:331px;overflow:hidden;background:var(--white);box-shadow:0 1px 3px rgba(0,0,0,.12)}
.col-a{left:6px}.col-b{left:606px}
.row-1{top:6px}.row-2{top:349px}.row-3{top:692px}.row-4{top:1035px}.row-5{top:1378px}.row-6{top:1721px}.row-7{top:2064px}
.abs{position:absolute}

/* brand stand-in */
.brand{position:absolute;display:flex;align-items:center;gap:5px;color:var(--white);font-weight:400;font-size:11px;letter-spacing:.6px;white-space:nowrap}
.brand .mark{width:9px;height:9px;background:currentColor}
.brand.center{transform:translateX(-50%)}
.brand.small{font-size:8px;gap:4px;color:var(--navy)}
.brand.small .mark{width:7px;height:7px;background:var(--teal)}

.rule{position:absolute;height:1px;background:rgba(255,255,255,.45)}
.url{position:absolute;top:31px;right:30px;font-size:6.5px;color:var(--white);display:flex;align-items:center;gap:8px}
.url::after{content:"";width:22px;height:1px;background:rgba(255,255,255,.6)}

.cover-title{position:absolute;text-align:center;color:var(--white);font-weight:400;font-size:22px;line-height:1.2;letter-spacing:.3px}
.cover-sub{position:absolute;text-align:center;color:var(--teal-bright);font-size:12px;letter-spacing:.3px}

/* white slide chrome */
.slide-title{position:absolute;left:29px;top:17px;font-size:20px;font-weight:400;color:var(--navy)}
.slide-title::after{content:"";position:absolute;left:0;top:31px;width:46px;height:1px;background:var(--teal)}
.footer-line{position:absolute;left:0;right:0;top:314px;height:1px;background:var(--teal-light)}
.footer .brand{left:31px;top:303px}
.copyright{position:absolute;right:30px;top:309px;font-size:4.6px;color:var(--ink);background:var(--white);padding:0 4px;display:flex;gap:6px}
.copyright .page{color:var(--teal)}

/* photo placeholders */
.photo-city{background:linear-gradient(160deg,#1a2c3e 0%,#0c1824 55%,#1d2a36 100%)}
.photo-tech{background:radial-gradient(ellipse at 55% 25%,#8fd3e0 0%,#2f7f98 30%,#123a52 70%,#0a2438 100%)}
.photo-circuit{background:radial-gradient(ellipse at 5% 60%,#2fb5ff 0%,#0e5fa0 22%,#0a3566 50%,transparent 75%)}
.photo-globe{background:radial-gradient(ellipse at 50% 100%,#2a6fa8 0%,#0e3b6a 40%,#07284a 62%,transparent 63%)}
.photo-hands{background:linear-gradient(135deg,#e9ecef 0%,#d5c7bd 45%,#b99f8e 70%,#e1e4e7 100%)}

/* agenda rows */
.agenda-row{position:absolute;left:31px;width:532px;height:45px}
.agenda-row .left{position:absolute;left:0;top:0;width:275px;height:45px;background:var(--navy)}
.agenda-row .right{position:absolute;left:255px;top:0;width:277px;height:45px;background:var(--teal);border-radius:0 23px 23px 0}
.agenda-row .mic{position:absolute;left:10px;top:15px}
.agenda-row .divider{position:absolute;left:32px;top:7px;width:1px;height:31px;background:rgba(255,255,255,.35)}
.agenda-row .topic{position:absolute;left:42px;top:6px;color:var(--white);font-size:11px;line-height:1.05}
.agenda-row .topic small{display:block;font-size:7px;margin-top:2px}
.agenda-row .topic em{display:block;font-style:normal;font-size:5.8px;margin-top:3px}
.agenda-row .num{position:absolute;left:236px;top:6px;width:33px;height:33px;border-radius:50%;background:var(--white);border:3px solid var(--navy);color:var(--navy);font-size:15px;display:flex;align-items:center;justify-content:center}
.agenda-row .info{position:absolute;left:285px;top:9px;width:230px;color:var(--white);font-size:7px;line-height:1.2}
.agenda-row .info b{display:block;font-weight:400;font-size:7px}

.agenda-item{position:absolute;width:220px}
.agenda-item .dot{position:absolute;left:0;top:0;width:22px;height:22px;border-radius:50%;background:var(--teal);display:flex;align-items:center;justify-content:center}
.agenda-item h4{position:absolute;left:35px;top:-3px;font-weight:400;font-size:11.5px;color:var(--navy)}
.agenda-item .time{position:absolute;left:35px;top:11px;font-size:7px;color:var(--teal)}
.agenda-item p{position:absolute;left:35px;top:19px;width:180px;font-size:5.8px;line-height:1.35;color:var(--body)}

/* feature panel */
.panel{position:absolute;color:var(--white)}
.panel h3{font-weight:400;font-size:16px;margin-bottom:13px}
.panel p{font-size:8.7px;line-height:1.3;margin-bottom:9px}

.tile{position:absolute;width:163px;height:98px;color:var(--white);padding:18px 12px 0}
.tile h5{font-weight:400;font-size:9.5px;margin-bottom:7px}
.tile p{font-size:6px;line-height:1.3}
.tile.teal{background:var(--teal)}.tile.navy{background:var(--navy)}

/* bar charts */
.bar-chart{position:absolute;top:76px;width:126px}
.plot{position:relative;width:126px;height:95px;background-color:var(--grid);background-image:linear-gradient(90deg,var(--white) 1px,transparent 1px),linear-gradient(0deg,var(--white) 1px,transparent 1px);background-size:18px 12px}
.plot svg{position:absolute;left:0;top:0}
.days{display:flex;width:126px;margin-top:2px}
.days span{flex:1;text-align:center;font-size:5px;color:var(--ink)}
.chart-label{text-align:center;margin-top:11px}
.chart-label h6{font-size:11px;font-weight:700;letter-spacing:.2px}
.chart-label p{font-size:6px;line-height:1.2;color:var(--ink);width:110px;margin:2px auto 0}
.navy-t{color:var(--navy)}.teal-t{color:var(--teal)}.grey-t{color:var(--grey)}

.gauge{position:absolute;top:113px;width:110px;text-align:center}
.gauge svg{display:block;margin:0 auto}
.gauge .pct{position:absolute;left:0;right:0;top:32px;font-size:14px;font-weight:700}

.donut{position:absolute}
.donut .pct{position:absolute;left:0;right:0;text-align:center;font-weight:700}

/* text slide */
.lead{position:absolute;left:30px;top:101px;width:530px;font-size:14px;line-height:1.25;color:var(--navy)}
.copy{position:absolute;left:30px;width:535px;font-size:8.7px;line-height:1.35;color:var(--body)}

.section-title{position:absolute;left:330px;width:232px;top:191px;text-align:center;color:var(--white);font-size:21px;letter-spacing:.3px}
</style>
</head>
<body>

<!-- 1 Cover: circuit -->
<section class="slide col-a row-1" style="background:linear-gradient(120deg,#0a2f57 0%,#072341 60%,#051a30 100%)">
  <div class="abs photo-circuit" style="left:0;top:0;width:330px;height:331px" role="img" aria-label="Glowing blue circuit-board lines"></div>
  <div class="url">www.marenaubel-conseil.fr</div>
  <div class="brand center" style="left:446px;top:138px"><span class="mark"></span>Maren Aubel</div>
  <div class="rule" style="left:331px;width:237px;top:170px"></div>
  <h1 class="cover-title" style="left:331px;width:237px;top:185px">TITLE PRESENTATION<br>GOES HERE</h1>
  <div class="rule" style="left:331px;width:237px;top:253px"></div>
  <div class="cover-sub" style="left:331px;width:237px;top:274px">SUBTITLE GOES HERE</div>
</section>

<!-- 2 Cover: globe -->
<section class="slide col-b row-1" style="background:linear-gradient(180deg,#0f8190 0%,#0b5d78 55%,#07375a 100%)">
  <div class="abs photo-globe" style="left:0;top:190px;width:588px;height:141px" role="img" aria-label="Earth seen from space with network arcs"></div>
  <div class="brand center" style="left:294px;top:58px"><span class="mark"></span>Maren Aubel</div>
  <h1 class="cover-title" style="left:150px;width:288px;top:93px">TITLE PRESENTATION<br>GOES HERE</h1>
  <div class="rule" style="left:180px;width:228px;top:154px"></div>
  <div class="cover-sub" style="left:150px;width:288px;top:163px;color:#3fc0cf">SUBTITLE GOES HERE</div>
  <div class="rule" style="left:180px;width:228px;top:186px"></div>
  <div class="abs" style="left:0;right:0;top:294px;text-align:center;font-size:6.5px;color:var(--white)">www.marenaubel-conseil.fr</div>
</section>

<!-- 3 Cover: city -->
<section class="slide col-a row-2 photo-city" role="img" aria-label="Night city skyline with security icons">
  <div class="url">www.marenaubel-conseil.fr</div>
  <div class="brand center" style="left:416px;top:102px"><span class="mark"></span>Maren Aubel</div>
  <h1 class="cover-title" style="left:290px;width:252px;top:144px">TITLE PRESENTATION<br>GOES HERE</h1>
  <div class="rule" style="left:300px;width:232px;top:208px"></div>
  <div class="cover-sub" style="left:290px;width:252px;top:215px;font-size:14px">SUBTITLE GOES HERE</div>
  <div class="rule" style="left:300px;width:232px;top:238px"></div>
</section>

<!-- 4 Agenda rows -->
<section class="slide col-b row-2">
  <h2 class="slide-title">Our Agenda</h2>
  <div class="agenda-row" style="top:71px">
    <div class="right"></div><div class="left"></div>
    <svg class="mic" width="12" height="14" viewBox="0 0 12 14"><rect x="4" y="0.5" width="4" height="7" rx="2" fill="none" stroke="#fff"/><path d="M2 6a4 4 0 0 0 8 0M6 10v3M4 13h4" fill="none" stroke="#fff"/></svg>
    <div class="divider"></div>
    <div class="topic">Your Topic Goes Here<small>10:00</small><em>Presented by: John Smith.</em></div>
    <div class="num">1</div>
    <div class="info"><b>Additional Info</b>Lorem ipsum dolor sit amet, consectetur adipiscing elit, sed do eiusmod tempor labore.</div>
  </div>
  <div class="agenda-row" style="top:122px">
    <div class="right"></div><div class="left"></div>
    <svg class="mic" width="12" height="14" viewBox="0 0 12 14"><rect x="4" y="0.5" width="4" height="7" rx="2" fill="none" stroke="#fff"/><path d="M2 6a4 4 0 0 0 8 0M6 10v3M4 13h4" fill="none" stroke="#fff"/></svg>
    <div class="divider"></div>
    <div class="topic">Your Topic Goes Here<small>10:00</small><em>Presented by: John Smith.</em></div>
    <div class="num">2</div>
    <div class="info"><b>Additional Info</b>Lorem ipsum dolor sit amet, consectetur adipiscing elit, sed do eiusmod tempor labore.</div>
  </div>
  <div class="agenda-row" style="top:172px">
    <div class="right"></div><div class="left"></div>
    <svg class="mic" width="12" height="14" viewBox="0 0 12 14"><rect x="4" y="0.5" width="4" height="7" rx="2" fill="none" stroke="#fff"/><path d="M2 6a4 4 0 0 0 8 0M6 10v3M4 13h4" fill="none" stroke="#fff"/></svg>
    <div class="divider"></div>
    <div class="topic">Your Topic Goes Here<small>10:00</small><em>Presented by: John Smith.</em></div>
    <div class="num">3</div>
    <div class="info"><b>Additional Info</b>Lorem ipsum dolor sit amet, consectetur adipiscing elit, sed do eiusmod tempor labore.</div>
  </div>
  <div class="agenda-row" style="top:223px">
    <div class="right"></div><div class="left"></div>
    <svg class="mic" width="12" height="14" viewBox="0 0 12 14"><rect x="4" y="0.5" width="4" height="7" rx="2" fill="none" stroke="#fff"/><path d="M2 6a4 4 0 0 0 8 0M6 10v3M4 13h4" fill="none" stroke="#fff"/></svg>
    <div class="divider"></div>
    <div class="topic">Your Topic Goes Here<small>10:00</small><em>Presented by: John Smith.</em></div>
    <div class="num">4</div>
    <div class="info"><b>Additional Info</b>Lorem ipsum dolor sit amet, consectetur adipiscing elit, sed do eiusmod tempor labore.</div>
  </div>
  <div class="footer"><div class="footer-line"></div><div class="brand small"><span class="mark"></span>Maren Aubel</div><div class="copyright">© Copyright 2021 Maren Aubel. Allright Reserved.<span class="page">| 4</span></div></div>
</section>

<!-- 5 Agenda list -->
<section class="slide col-a row-3">
  <h2 class="slide-title">Our Agenda</h2>
  <div class="agenda-item" style="left:79px;top:91px"><div class="dot"><svg width="9" height="11" viewBox="0 0 12 14"><rect x="4" y="0.5" width="4" height="7" rx="2" fill="none" stroke="#fff" stroke-width="1.4"/><path d="M2 6a4 4 0 0 0 8 0M6 10v3M4 13h4" fill="none" stroke="#fff" stroke-width="1.4"/></svg></div><h4>Agenda One</h4><div class="time">10:00</div><p>Lorem ipsum dolor sit amet, consectetur adipiscing elit, sed do eiusmod tempor labore.</p></div>
  <div class="agenda-item" style="left:79px;top:161px"><div class="dot"><svg width="9" height="11" viewBox="0 0 12 14"><rect x="4" y="0.5" width="4" height="7" rx="2" fill="none" stroke="#fff" stroke-width="1.4"/><path d="M2 6a4 4 0 0 0 8 0M6 10v3M4 13h4" fill="none" stroke="#fff" stroke-width="1.4"/></svg></div><h4>Agenda Two</h4><div class="time">11:00</div><p>Lorem ipsum dolor sit amet, consectetur adipiscing elit, sed do eiusmod tempor labore.</p></div>
  <div class="agenda-item" style="left:79px;top:228px"><div class="dot"><svg width="9" height="11" viewBox="0 0 12 14"><rect x="4" y="0.5" width="4" height="7" rx="2" fill="none" stroke="#fff" stroke-width="1.4"/><path d="M2 6a4 4 0 0 0 8 0M6 10v3M4 13h4" fill="none" stroke="#fff" stroke-width="1.4"/></svg></div><h4>Agenda Three</h4><div class="time">12:00</div><p>Lorem ipsum dolor sit amet, consectetur adipiscing elit, sed do eiusmod tempor labore.</p></div>
  <div class="agenda-item" style="left:317px;top:91px"><div class="dot"><svg width="9" height="11" viewBox="0 0 12 14"><rect x="4" y="0.5" width="4" height="7" rx="2" fill="none" stroke="#fff" stroke-width="1.4"/><path d="M2 6a4 4 0 0 0 8 0M6 10v3M4 13h4" fill="none" stroke="#fff" stroke-width="1.4"/></svg></div><h4>Agenda Four</h4><div class="time">13:00</div><p>Lorem ipsum dolor sit amet, consectetur adipiscing elit, sed do eiusmod tempor labore.</p></div>
  <div class="agenda-item" style="left:317px;top:161px"><div class="dot"><svg width="9" height="11" viewBox="0 0 12 14"><rect x="4" y="0.5" width="4" height="7" rx="2" fill="none" stroke="#fff" stroke-width="1.4"/><path d="M2 6a4 4 0 0 0 8 0M6 10v3M4 13h4" fill="none" stroke="#fff" stroke-width="1.4"/></svg></div><h4>Agenda Five</h4><div class="time">14:00</div><p>Lorem ipsum dolor sit amet, consectetur adipiscing elit, sed do eiusmod tempor labore.</p></div>
  <div class="agenda-item" style="left:317px;top:228px"><div class="dot"><svg width="9" height="11" viewBox="0 0 12 14"><rect x="4" y="0.5" width="4" height="7" rx="2" fill="none" stroke="#fff" stroke-width="1.4"/><path d="M2 6a4 4 0 0 0 8 0M6 10v3M4 13h4" fill="none" stroke="#fff" stroke-width="1.4"/></svg></div><h4>Agenda Six</h4><div class="time">15:00</div><p>Lorem ipsum dolor sit amet, consectetur adipiscing elit, sed do eiusmod tempor labore.</p></div>
  <div class="footer"><div class="footer-line"></div><div class="brand small"><span class="mark"></span>Maren Aubel</div><div class="copyright">© Copyright 2021 Maren Aubel. Allright Reserved.<span class="page">| 5</span></div></div>
</section>

<!-- 6 Image + text panel -->
<section class="slide col-b row-3">
  <h2 class="slide-title">Title Goes Here</h2>
  <div class="abs photo-tech" style="left:0;top:74px;width:294px;height:186px" role="img" aria-label="Digital globe over a glowing city skyline"></div>
  <div class="abs" style="left:294px;top:74px;width:294px;height:186px;background:var(--navy)"></div>
  <div class="panel" style="left:323px;top:97px;width:250px">
    <h3>Heading Here</h3>
    <p>Lorem ipsum dolor sit amet, consectetur adipiscing elit, sed do eiusmod tempor incididunt ut labore et dolore magna aliqua. Ut enimad minim veniam, quis nostrud exercitation ullamco laboris nisi ut aliquip ex ea commodo consequat.</p>
    <p>Excepteur sint occaecat cupidatat non proident, sunt inculpa qui officia deserunt mollit anim id est laborum.</p>
  </div>
  <div class="footer"><div class="footer-line"></div><div class="brand small"><span class="mark"></span>Maren Aubel</div><div class="copyright">© Copyright 2021 Maren Aubel. Allright Reserved.<span class="page">| 6</span></div></div>
</section>

<!-- 7 Section divider navy -->
<section class="slide col-a row-4" style="background:var(--navy)">
  <div class="brand center" style="left:420px;top:136px"><span class="mark"></span>Maren Aubel</div>
  <div class="rule" style="left:330px;width:232px;top:171px"></div>
  <h2 class="section-title">SECTION DIVIDER</h2>
</section>

<!-- 8 Section divider teal -->
<section class="slide col-b row-4" style="background:var(--teal)">
  <div class="brand center" style="left:420px;top:136px"><span class="mark"></span>Maren Aubel</div>
  <div class="rule" style="left:330px;width:232px;top:171px"></div>
  <h2 class="section-title">SECTION DIVIDER</h2>
</section>

<!-- 9 Tile grid -->
<section class="slide col-a row-5">
  <h2 class="slide-title">Your Title Goes Here</h2>
  <div class="tile photo-city" style="left:42px;top:73px;padding:0" role="img" aria-label="City at night with connected network icons"></div>
  <div class="tile teal" style="left:212px;top:73px"><h5>Heading Goes Here</h5><p>Lorem Ipsum dolor sit amer, consectetur adipiscing elit, sed do eiusmod tempor incididunt ut labore et commodo consequat dolore magna aliqua.</p></div>
  <div class="tile photo-tech" style="left:381px;top:73px;padding:0" role="img" aria-label="Digital globe above city skyline"></div>
  <div class="tile navy" style="left:42px;top:177px"><h5>Heading Goes Here</h5><p>Lorem Ipsum dolor sit amer, consectetur adipiscing elit, sed do eiusmod tempor incididunt ut labore et commodo consequat dolore magna aliqua.</p></div>
  <div class="tile photo-hands" style="left:212px;top:177px;padding:0" role="img" aria-label="Team members joining hands"></div>
  <div class="tile navy" style="left:381px;top:177px"><h5>Heading Goes Here</h5><p>Lorem Ipsum dolor sit amer, consectetur adipiscing elit, sed do eiusmod tempor incididunt ut labore et commodo consequat dolore magna aliqua.</p></div>
  <div class="footer"><div class="footer-line"></div><div class="brand small"><span class="mark"></span>Maren Aubel</div><div class="copyright">© Copyright 2021 Maren Aubel. Allright Reserved.<span class="page">| 9</span></div></div>
</section>

<!-- 10 Bar charts -->
<section class="slide col-b row-5">
  <h2 class="slide-title">Our Chart #1</h2>
  <div class="bar-chart" style="left:56px">
    <div class="plot"><svg width="126" height="95" font-family="Lato,sans-serif" font-size="4.5" fill="#0a3150" text-anchor="middle">
      <rect x="0" y="47.5" width="17" height="47.5"/><rect x="18" y="59.8" width="17" height="35.2"/><rect x="36" y="48.4" width="17" height="46.6"/><rect x="54" y="26.6" width="17" height="68.4"/><rect x="72" y="64.6" width="17" height="30.4"/><rect x="90" y="47.5" width="17" height="47.5"/><rect x="108" y="85.5" width="17" height="9.5"/>
      <g fill="#1f2b36"><text x="8.5" y="45">50%</text><text x="26.5" y="57">37%</text><text x="44.5" y="46">49%</text><text x="62.5" y="24">72%</text><text x="80.5" y="62">32%</text><text x="98.5" y="45">50%</text><text x="116.5" y="83">10%</text></g>
    </svg></div>
    <div class="days"><span>Sun</span><span>Mon</span><span>Tue</span><span>Wed</span><span>Thu</span><span>Fri</span><span>Sat</span></div>
    <div class="chart-label"><h6 class="navy-t">INFODATA 01</h6><p>Lorem ipsum dolor sit amet, consectetur adipiscing elit, sed do eiusmod tempor</p></div>
  </div>
  <div class="bar-chart" style="left:227px">
    <div class="plot"><svg width="126" height="95" font-family="Lato,sans-serif" font-size="4.5" fill="#0f8c9d" text-anchor="middle">
      <rect x="0" y="64.6" width="17" height="30.4"/><rect x="18" y="41.8" width="17" height="53.2"/><rect x="36" y="10.4" width="17" height="84.6"/><rect x="54" y="55.1" width="17" height="39.9"/><rect x="72" y="80.7" width="17" height="14.3"/><rect x="90" y="46.5" width="17" height="48.5"/><rect x="108" y="73.1" width="17" height="21.9"/>
      <g fill="#1f2b36"><text x="8.5" y="62">32%</text><text x="26.5" y="39">56%</text><text x="44.5" y="8">89%</text><text x="62.5" y="53">42%</text><text x="80.5" y="78">15%</text><text x="98.5" y="44">51%</text><text x="116.5" y="71">23%</text></g>
    </svg></div>
    <div class="days"><span>Sun</span><span>Mon</span><span>Tue</span><span>Wed</span><span>Thu</span><span>Fri</span><span>Sat</span></div>
    <div class="chart-label"><h6 class="teal-t">INFODATA 02</h6><p>Lorem ipsum dolor sit amet, consectetur adipiscing elit, sed do eiusmod tempor</p></div>
  </div>
  <div class="bar-chart" style="left:395px">
    <div class="plot"><svg width="126" height="95" font-family="Lato,sans-serif" font-size="4.5" fill="#a7a7a7" text-anchor="middle">
      <rect x="0" y="53.2" width="17" height="41.8"/><rect x="18" y="82.6" width="17" height="12.4"/><rect x="36" y="35.1" width="17" height="59.9"/><rect x="54" y="67.4" width="17" height="27.6"/><rect x="72" y="61.7" width="17" height="33.3"/><rect x="90" y="20.9" width="17" height="74.1"/><rect x="108" y="40.8" width="17" height="54.2"/>
      <g fill="#c2c2c2"><text x="8.5" y="51">44%</text><text x="26.5" y="80">13%</text><text x="44.5" y="33">63%</text><text x="62.5" y="65">29%</text><text x="80.5" y="59">35%</text><text x="98.5" y="19">78%</text><text x="116.5" y="38">57%</text></g>
    </svg></div>
    <div class="days"><span>Sun</span><span>Mon</span><span>Tue</span><span>Wed</span><span>Thu</span><span>Fri</span><span>Sat</span></div>
    <div class="chart-label"><h6 class="grey-t">INFODATA 03</h6><p>Lorem ipsum dolor sit amet, consectetur adipiscing elit, sed do eiusmod tempor</p></div>
  </div>
  <div class="footer"><div class="footer-line"></div><div class="brand small"><span class="mark"></span>Maren Aubel</div><div class="copyright">© Copyright 2021 Maren Aubel. Allright Reserved.<span class="page">| 10</span></div></div>
</section>

<!-- 11 Gauges -->
<section class="slide col-a row-6">
  <h2 class="slide-title">Our Chart #2</h2>
  <div class="gauge" style="left:54px">
    <svg width="100" height="54" viewBox="0 0 100 54"><path d="M8 50A42 42 0 0 1 92 50" fill="none" stroke="#a7b9c6" stroke-width="9"/><path d="M8 50A42 42 0 0 1 12.6 30.9" fill="none" stroke="#0a3150" stroke-width="9"/></svg>
    <div class="pct navy-t">15%</div>
    <div class="chart-label" style="margin-top:8px"><h6 class="navy-t">INFODATA 01</h6><p>Lorem ipsum dolor sit amet, consectetur adipiscing elit, sed do eiusmod tempor</p></div>
  </div>
  <div class="gauge" style="left:180px">
    <svg width="100" height="54" viewBox="0 0 100 54"><path d="M8 50A42 42 0 0 1 92 50" fill="none" stroke="#a9dbe2" stroke-width="9"/><path d="M8 50A42 42 0 0 1 46.1 8.2" fill="none" stroke="#0f8c9d" stroke-width="9"/></svg>
    <div class="pct teal-t">47%</div>
    <div class="chart-label" style="margin-top:8px"><h6 class="teal-t">INFODATA 02</h6><p>Lorem ipsum dolor sit amet, consectetur adipiscing elit, sed do eiusmod tempor</p></div>
  </div>
  <div class="gauge" style="left:306px">
    <svg width="100" height="54" viewBox="0 0 100 54"><path d="M8 50A42 42 0 0 1 92 50" fill="none" stroke="#e2e2e2" stroke-width="9"/><path d="M8 50A42 42 0 0 1 63 10.1" fill="none" stroke="#a7a7a7" stroke-width="9"/></svg>
    <div class="pct grey-t">60%</div>
    <div class="chart-label" style="margin-top:8px"><h6 class="grey-t">INFODATA 03</h6><p>Lorem ipsum dolor sit amet, consectetur adipiscing elit, sed do eiusmod tempor</p></div>
  </div>
  <div class="gauge" style="left:432px">
    <svg width="100" height="54" viewBox="0 0 100 54"><path d="M8 50A42 42 0 0 1 92 50" fill="none" stroke="#a7b9c6" stroke-width="9"/><path d="M8 50A42 42 0 0 1 86.2 28.6" fill="none" stroke="#0a3150" stroke-width="9"/></svg>
    <div class="pct navy-t">83%</div>
    <div class="chart-label" style="margin-top:8px"><h6 class="navy-t">INFODATA 04</h6><p>Lorem ipsum dolor sit amet, consectetur adipiscing elit, sed do eiusmod tempor</p></div>
  </div>
  <div class="footer"><div class="footer-line"></div><div class="brand small"><span class="mark"></span>Maren Aubel</div><div class="copyright">© Copyright 2021 Maren Aubel. Allright Reserved.<span class="page">| 11</span></div></div>
</section>

<!-- 12 Donuts -->
<section class="slide col-b row-6">
  <h2 class="slide-title">Our Chart #3</h2>
  <svg class="abs" style="left:0;top:0" width="588" height="331">
    <path d="M222 162Q296 208 370 162" fill="none" stroke="#9aa3ab" stroke-width="1.2" stroke-dasharray="1.5 3.5"/>
    <circle cx="222" cy="162" r="5" fill="#fff" stroke="#a7a7a7" stroke-width="1.4"/><circle cx="222" cy="162" r="2" fill="#a7a7a7"/>
    <circle cx="370" cy="162" r="5" fill="#fff" stroke="#0f8c9d" stroke-width="1.4"/><circle cx="370" cy="162" r="2" fill="#0f8c9d"/>
    <circle cx="296" cy="185" r="5" fill="#fff" stroke="#0a3150" stroke-width="1.4"/><circle cx="296" cy="185" r="2" fill="#0a3150"/>
    <!-- large 87 -->
    <circle cx="296" cy="112" r="51" fill="none" stroke="#e2e2e2" stroke-width="15"/>
    <circle cx="296" cy="112" r="51" fill="none" stroke="#0a3150" stroke-width="15" pathLength="100" stroke-dasharray="87 100" transform="rotate(-90 296 112)"/>
    <circle cx="296" cy="112" r="38" fill="#fff"/>
    <!-- 15 -->
    <circle cx="177" cy="194" r="37" fill="#f2f2f2"/>
    <circle cx="177" cy="194" r="31" fill="none" stroke="#e6e6e6" stroke-width="9"/>
    <circle cx="177" cy="194" r="31" fill="none" stroke="#a7a7a7" stroke-width="9" pathLength="100" stroke-dasharray="15 100" transform="rotate(-90 177 194)"/>
    <circle cx="177" cy="194" r="24" fill="#fff"/>
    <!-- 32 -->
    <circle cx="407" cy="194" r="37" fill="#f2f2f2"/>
    <circle cx="407" cy="194" r="31" fill="none" stroke="#e6e6e6" stroke-width="9"/>
    <circle cx="407" cy="194" r="31" fill="none" stroke="#0f8c9d" stroke-width="9" pathLength="100" stroke-dasharray="32 100" transform="rotate(-90 407 194)"/>
    <circle cx="407" cy="194" r="24" fill="#fff"/>
    <!-- 40 -->
    <circle cx="295" cy="254" r="37" fill="#f2f2f2"/>
    <circle cx="295" cy="254" r="31" fill="none" stroke="#e6e6e6" stroke-width="9"/>
    <circle cx="295" cy="254" r="31" fill="none" stroke="#0a3150" stroke-width="9" pathLength="100" stroke-dasharray="40 100" transform="rotate(-90 295 254)"/>
    <circle cx="295" cy="254" r="24" fill="#fff"/>
  </svg>
  <div class="donut navy-t" style="left:246px;top:100px;width:100px"><div class="pct" style="font-size:19px">87%</div></div>
  <div class="donut grey-t" style="left:147px;top:187px;width:60px"><div class="pct" style="font-size:12px;font-weight:400">15%</div></div>
  <div class="donut teal-t" style="left:377px;top:187px;width:60px"><div class="pct" style="font-size:12px">32%</div></div>
  <div class="donut navy-t" style="left:265px;top:246px;width:60px"><div class="pct" style="font-size:12px">40%</div></div>
  <div class="footer"><div class="footer-line"></div><div class="brand small"><span class="mark"></span>Maren Aubel</div><div class="copyright">© Copyright 2021 Maren Aubel. Allright Reserved.<span class="page">| 12</span></div></div>
</section>

<!-- 13 Text slide -->
<section class="slide col-a row-7">
  <h2 class="slide-title">Our Text Slide</h2>
  <p class="lead">This is place for your header text. Insert your text here, just replace this text with your own text</p>
  <p class="copy" style="top:157px">Lorem ipsum dolor sit amet, consectetur adipiscing elit, sed do eiusmod tempor incididunt ut labore et dolore magna aliqua. Ut enimad minim veniam, quis nostrud exercitation ullamco laboris nisi ut aliquip ex ea commodo consequat.</p>
  <p class="copy" style="top:191px">Duis aute irure dolor in reprehenderit in voluptate velit esse cillum dolore eu fugiat nulla pariatur. Ut enimad minim veniam, quis nostrud exercitation ullamco laboris nisi ut aliquip ex ea commodo consequat..<br>Excepteur sint occaecat cupidatat non proident, sunt inculpa qui officia deserunt mollit anim id est laborum.</p>
  <p class="copy" style="top:238px">Ut enimad minim veniam, quis nostrud exercitation ullamco laboris nisi ut aliquip ex ea commodo consequat. Lorem ipsum dolor sit amet, consectetur adipiscing elit, sed do eiusmod tempor incididunt ut labore et dolore magna aliqua.</p>
  <div class="footer"><div class="footer-line"></div><div class="brand small"><span class="mark"></span>Maren Aubel</div><div class="copyright">© Copyright 2021 Maren Aubel. Allright Reserved.<span class="page">| 13</span></div></div>
</section>

<!-- 14 Closing -->
<section class="slide col-b row-7 photo-city" role="img" aria-label="Aerial night city with security icons">
  <div class="url">www.marenaubel-conseil.fr</div>
  <div class="brand center" style="left:416px;top:150px"><span class="mark"></span>Maren Aubel</div>
  <h2 class="abs" style="left:290px;width:252px;top:186px;text-align:center;color:var(--white);font-weight:400;font-size:36px;letter-spacing:.5px">THANK YOU</h2>
</section>

</body>
</html>
```